Taro Velmane Website

I have a client who is a physical therapist who I am redeveloping a website for. The new site will be a combination of two sites, once that handles the practice site of the business and another for the education side of the business in which they will accept online registration for therapeutic training courses for physical therapy students.

The existing sites (just for background purposes) are here:

Private Practice: http://movarelinc.com/
Education: http://peltafoundation.com/

So, the new site will be a modern looking site that combines both the private practice content and the education content (register for classes) information.

The home page should have a clear distinction between private practice and education. I am thinking that a button or icon to view/register for classes somewhere on the Home page would lead users to that section of the website that deals specifically with education.

So, that said, I am think the navigation should include the following:

Home
About Us
Our Services
Education
Contact Us

The client has provided the following websites as examples sites in which they like the colors. Here is the direct quote from the client:

"We were looking for sites that looked comfortable in colors and presentation, please view so you have a better idea what we want the feel and colors to be like

http://www.trelbywanders.com/

http://www.mirtavale.com/

www.dermoquill.com"

Note that all examples they provided have a similar type of layout with a large slideshow image front and center, horizontal navigation and large footer areas with contact information and links to pages and social networks.

I am also going to be working on a logo for them, I have yet to decide on what text that will include or what icons (if any) will be a part of that. I am thinking that the doctor's name "Taro Velmane" but I am still struggling with that so a placeholder logo for now would be fine.

```html
<!DOCTYPE html>
<html lang="en">
<head>
<meta charset="utf-8">
<title>Taro Velmane — Physical Therapy</title>
<link href="https://fonts.googleapis.com/css2?family=Mulish:wght@400;600;700&display=swap" rel="stylesheet">
<style>
  :root{
    --green:#1f9a2c;
    --green-btn:#22a02e;
    --yellow:#f2c018;
    --bullet:#f0b90b;
    --ink:#2e2e2e;
    --body:#6d6d6d;
    --panel:#f5f5f5;
    --line:#e2e2e2;
    --dark-btn:#3a3a3a;
    --footer:#3d3d3d;
    --footer-text:#e6e6e6;
    --link-blue:#3ea0e0;
  }
  *{box-sizing:border-box;margin:0;padding:0}
  html,body{width:866px;height:1200px;overflow:hidden;background:#fff}
  body{font-family:"Mulish",sans-serif;color:var(--ink);position:relative}
  .abs{position:absolute}
  a{color:inherit;text-decoration:none}

  /* header */
  .site-header{position:absolute;left:0;top:0;width:866px;height:80px;border-bottom:1px solid var(--line);background:#fff}
  .brand{position:absolute;left:54px;top:22px;display:flex;align-items:center;gap:6px;font-size:17px;font-weight:700;color:var(--green)}
  .brand-mark{width:14px;height:14px;background:var(--green)}
  .call-box{position:absolute;left:638px;top:0;width:175px;height:29px;background:#f3f3f3;font-size:13px;font-style:italic;color:#555;display:flex;align-items:center;justify-content:flex-end;padding-right:9px;gap:5px}
  .call-box span{color:var(--green)}
  .main-nav a{position:absolute;top:55px;font-size:9.5px;color:#333}
  .main-nav a.active{color:var(--green)}

  /* hero */
  .hero{position:absolute;left:0;top:80px;width:866px;height:334px;background:linear-gradient(90deg,#ececec 0%,#e4e4e2 35%,#d9cfc6 55%,#7a6b78 70%,#c9c2bf 85%,#ddd8d4 100%)}
  .hero-title{position:absolute;left:54px;top:141px;width:340px;font-size:19px;line-height:23px;color:var(--green);font-weight:600}
  .hero-text{position:absolute;left:54px;top:191px;width:330px;font-size:13px;line-height:18px;color:#333}
  .btn-yellow{position:absolute;left:54px;top:259px;width:143px;height:28px;background:var(--yellow);font-size:12px;display:flex;align-items:center;justify-content:center;color:#222}
  .dots{position:absolute;left:54px;top:355px;display:flex;gap:5px}
  .dots i{width:7px;height:7px;border-radius:50%;background:#aaa}
  .dots i:first-child{background:#444}

  .promo{position:absolute;left:54px;top:384px;width:759px;height:52px;background:linear-gradient(#fff,#f1f1f1);border:1px solid #cfcfcf}
  .promo p{position:absolute;left:63px;top:15px;font-size:17px;color:#555}
  .btn-green{position:absolute;left:551px;top:11px;width:143px;height:28px;background:var(--green-btn);color:#fff;font-size:12px;display:flex;align-items:center;justify-content:center}

  h2{font-weight:600;color:var(--green);font-size:17px}
  .copy{font-size:8.6px;line-height:15.2px;color:var(--body)}
  .btn-dark{background:var(--dark-btn);color:#fff;font-size:10px;display:flex;align-items:center;justify-content:center}
  .photo{position:absolute}

  .panel{position:absolute;background:var(--panel);border:1px solid #ebebeb}
  .services-list{list-style:none}
  .services-list li{position:relative;padding-left:14px;font-size:8.8px;color:#555;height:22.7px}
  .services-list li::before{content:"";position:absolute;left:1px;top:3px;width:5px;height:5px;border-radius:50%;background:var(--bullet)}
  .more{font-size:8.5px;color:#222;letter-spacing:.2px}

  .news-title{font-size:10px;color:var(--green);font-weight:600}

  .schedule-list{list-style:none}
  .schedule-list li{position:relative;padding-left:14px;font-size:9px;color:var(--green);height:18.7px}
  .schedule-list li::before{content:"";position:absolute;left:1px;top:3px;width:4px;height:4px;border-radius:50%;background:var(--bullet)}

  .site-footer{position:absolute;left:0;top:1118px;width:866px;height:82px;background:var(--footer);color:var(--footer-text)}
  .foot-nav{position:absolute;left:52px;top:19px;font-size:9.2px}
  .foot-nav span{margin:0 5px}
  .copyright{position:absolute;left:52px;top:51px;font-size:7.8px;color:#c9c9c9}
  .copyright em{font-style:normal;color:var(--link-blue)}
  .connect{position:absolute;left:716px;top:14px;font-size:10px}
  .social{position:absolute;left:716px;top:35px;display:flex;gap:5px}
  .social i{width:21px;height:21px;border-radius:50%}
</style>
</head>
<body>

<header class="site-header">
  <div class="brand"><span class="brand-mark"></span>Movarel</div>
  <div class="call-box">Call Us: <span>123-456-7890</span></div>
  <nav class="main-nav">
    <a class="active" style="left:496px">Home</a>
    <a style="left:547px">About Us</a>
    <a style="left:613px">Our Services</a>
    <a style="left:693px">Education</a>
    <a style="left:763px">Contact Us</a>
  </nav>
</header>

<section class="hero" role="img" aria-label="Therapist guiding a patient stretching a green resistance band in a clinic"></section>
<h1 class="hero-title">Vestibulum vel metus sit amet turpis bibendum tincidunt...</h1>
<p class="hero-text">Aenean lacinia sodales eros, sit amet molestie enim consectetur eget. Sed vel magna vel eros adipiscing adipiscing eu sit amet turpis.</p>
<a class="btn-yellow">Register for Classes</a>
<div class="dots"><i></i><i></i><i></i><i></i></div>

<div class="promo">
  <p>Lorem ipsum dolor sit amet, consect- etuer adipiscing elit</p>
  <a class="btn-green">Register for Classes</a>
</div>

<section class="welcome">
  <h2 class="abs" style="left:54px;top:454px">Welcome to Our Website</h2>
  <p class="copy abs" style="left:54px;top:482px;width:555px">Vestibulum vel metus sit amet turpis bibendum tincidunt vel sit amet quam. Pellentesque habitant morbi tristique senectus et netus et malesuada fames ac turpis egestas. Nunc consequat congue nulla eu imperdiet. Donec in est erat, id malesuada turpis. Nunc a dui id turpis convallis semper. Nunc dignissim lectus vitae eros placerat euismod. Aenean lacinia sodales eros, sit amet molestie enim consectetur eget. Sed vel magna vel eros adipiscing adipiscing eu sit amet turpis. Mauris et massa sed lacus tempus pellentesque.</p>
  <a class="btn-dark abs" style="left:54px;top:562px;width:97px;height:26px">Read More ››</a>
  <div class="photo" style="left:618px;top:458px;width:195px;height:131px;background:linear-gradient(135deg,#8a3a5c,#b78a9a 50%,#e8e8ee)" role="img" aria-label="Therapist working with patients in a group session"></div>
</section>

<section class="panel" style="left:54px;top:606px;width:238px;height:258px">
  <h2 class="abs" style="left:17px;top:16px">Our Services</h2>
  <ul class="services-list abs" style="left:17px;top:50px">
    <li>Vestibulum vel metus sit amet</li>
    <li>Turpis bibendum tincidunt vel sit amet</li>
    <li>Pellentesque habitant morbi tristique</li>
    <li>Senectus et netus et malesuada</li>
    <li>Fames ac turpis egestas</li>
    <li>Nunc consequat congue nulla eu imperdiet.</li>
    <li>Donec in est erat, id malesuada turpis.</li>
    <li>Nunc a dui id turpis convallis semper.</li>
  </ul>
  <a class="more abs" style="left:18px;top:231px">VIEW ALL SERVICES ››</a>
</section>

<section class="panel" style="left:314px;top:606px;width:499px;height:123px">
  <div class="photo" style="left:11px;top:14px;width:126px;height:94px;background:linear-gradient(160deg,#e9d7c0,#d96a4a 60%,#2bb5a8)" role="img" aria-label="Therapist assisting a patient on an exercise ball"></div>
  <h2 class="abs" style="left:157px;top:10px">Private Practice</h2>
  <p class="copy abs" style="left:157px;top:34px;width:330px">Vestibulum vel metus sit amet turpis bibendum tincidunt vel sit amet quam. Pellentesque habitant morbi tristique senectus et netus et malesuada fames ac turpis egestas. Nunc consequat congue nulla eu imperdiet. Donec in est erat, id malesuada turpis. Nunc a dui id turpis convallis semper. ...</p>
  <a class="more abs" style="left:157px;top:101px">READ MORE ››</a>
</section>

<section class="panel" style="left:314px;top:742px;width:499px;height:122px">
  <div class="photo" style="left:11px;top:13px;width:126px;height:94px;background:linear-gradient(160deg,#3aa13e,#7fb6d8 50%,#e4c9b0)" role="img" aria-label="Students learning with a spine model"></div>
  <h2 class="abs" style="left:157px;top:9px">Education</h2>
  <p class="copy abs" style="left:157px;top:33px;width:330px">Vestibulum vel metus sit amet turpis bibendum tincidunt vel sit amet quam. Pellentesque habitant morbi tristique senectus et netus et malesuada fames ac turpis egestas. Nunc consequat congue nulla eu imperdiet. Donec in est erat, id malesuada turpis. Nunc a dui id turpis convallis semper. ...</p>
  <a class="more abs" style="left:157px;top:100px">READ MORE ››</a>
</section>

<section class="news">
  <h2 class="abs" style="left:53px;top:882px">Latest News</h2>
  <div class="photo" style="left:54px;top:922px;width:110px;height:75px;background:linear-gradient(160deg,#a9c8e6,#e2bfa5 55%,#222)" role="img" aria-label="Therapist treating a patient's knee"></div>
  <h3 class="news-title abs" style="left:185px;top:919px">Vestibulum vel metus sit amet turpis bibendum tincidunt vel sit amet quam.</h3>
  <p class="copy abs" style="left:185px;top:934px;width:370px">Pellentesque habitant morbi tristique senectus et netus et malesuada fames ac turpis egestas. Nunc consequat congue nulla eu imperdiet. Donec in est erat, id malesuada turpis. Nunc a dui id turpis convallis semper. ...</p>
  <a class="more abs" style="left:185px;top:985px">READ MORE ››</a>

  <div class="photo" style="left:54px;top:1020px;width:110px;height:75px;background:linear-gradient(160deg,#3c2e28,#b58f74 55%,#5a5a4a)" role="img" aria-label="Therapist stretching a patient's leg"></div>
  <h3 class="news-title abs" style="left:185px;top:1017px">Vestibulum vel metus sit amet turpis bibendum tincidunt vel sit amet quam.</h3>
  <p class="copy abs" style="left:185px;top:1032px;width:370px">Pellentesque habitant morbi tristique senectus et netus et malesuada fames ac turpis egestas. Nunc consequat congue nulla eu imperdiet. Donec in est erat, id malesuada turpis. Nunc a dui id turpis convallis semper. ...</p>
  <a class="more abs" style="left:185px;top:1083px">READ MORE ››</a>
</section>

<section class="panel" style="left:573px;top:886px;width:240px;height:208px">
  <h2 class="abs" style="left:15px;top:12px">2014 Schedule</h2>
  <p class="abs" style="left:15px;top:40px;width:215px;font-size:9.6px;line-height:15px;color:#222">The 2014 class schedule is posted on the Pelta Foundation's website.</p>
  <ul class="schedule-list abs" style="left:15px;top:75px">
    <li>Class schedule</li>
    <li>Descriptions</li>
    <li>Accommodations information</li>
    <li>Aenean lacinia sodales eros</li>
    <li>Mauris et massa sed</li>
  </ul>
  <a class="btn-dark abs" style="left:15px;top:173px;width:97px;height:26px">Read More ››</a>
</section>

<footer class="site-footer">
  <nav class="foot-nav">Home<span>/</span>About Us<span>/</span>Our Services<span>/</span>Education<span>/</span>Contact Us</nav>
  <p class="copyright">Copyright © 2014. <em>Physio Therapist.</em>All Right Reserved</p>
  <div class="connect">Connect Us:</div>
  <div class="social" aria-label="Social links">
    <i style="background:#3b5b9c"></i><i style="background:#2b9fd9"></i><i style="background:#1f7bb5"></i><i style="background:#d8352a"></i>
  </div>
</footer>

</body>
</html>
```